" Somos uma empresa de pessoas jovens que tenta atender os clientes de forma ágil e flexível. Prestamos diversos serviços nas áreas indicadas e conforme powerpoint detalhado. "

```html
<!DOCTYPE html>
<html lang="pt-BR">
<head>
<meta charset="UTF-8">
<title>Nuvira Projetos – Gerenciamento & Consultoria</title>
<link href="https://fonts.googleapis.com/css2?family=Montserrat:wght@400;500;600;700;800&display=swap" rel="stylesheet">
<style>
  :root{
    --green-deep:#1d443d;
    --green:#2c6b5c;
    --green-soft:#4f8c7b;
    --ink:#2b2f2e;
    --muted:#7a8380;
    --line:#dfe4e2;
    --paper:#ffffff;
    --mist:#f3f5f4;
    --photo-a:#3d4f55;
    --photo-b:#8a9aa0;
  }
  *{box-sizing:border-box;margin:0;padding:0}
  html,body{width:1200px;height:1200px;overflow:hidden;background:var(--paper)}
  body{font-family:"Montserrat",sans-serif;color:var(--ink)}
  .page{width:1200px;height:1200px;display:flex;flex-direction:column}
  .page > *{flex:none}

  .site-header{height:64px;display:flex;align-items:center;justify-content:space-between;padding:0 60px;background:var(--paper)}
  .brand{display:flex;align-items:center;gap:10px;font-weight:700;font-size:18px;color:var(--green-deep);letter-spacing:.5px}
  .brand-dot{width:14px;height:14px;border-radius:50%;background:var(--green)}
  .main-nav{display:flex;gap:4px}
  .main-nav a{font-size:12px;font-weight:600;text-transform:uppercase;color:var(--ink);text-decoration:none;padding:8px 14px}
  .main-nav a.active{background:var(--green);color:#fff}

  .hero{position:relative;height:316px;overflow:hidden}
  .hero-photo{position:absolute;inset:0;background:linear-gradient(160deg,var(--photo-b) 0%,var(--photo-a) 70%,#2a3538 100%)}
  .hero-cut{position:absolute;left:0;bottom:0;width:1200px;height:90px}
  .hero-copy{position:absolute;left:120px;top:100px;color:#fff}
  .hero-title{font-size:26px;font-weight:800;line-height:1.25;text-transform:uppercase;letter-spacing:.5px}
  .hero-btn{display:inline-block;margin-top:20px;border:2px solid #fff;color:#fff;font-size:11px;font-weight:700;padding:8px 20px;letter-spacing:1px}

  .section-title{text-align:center;font-weight:800;font-size:20px;text-transform:uppercase;color:var(--green);letter-spacing:1px}
  .section-title::after{content:"";display:block;width:40px;height:3px;background:var(--green);margin:8px auto 0}

  .services{height:240px;padding-top:8px}
  .service-grid{display:flex;justify-content:center;gap:28px;margin-top:22px}
  .service-card{width:200px}
  .service-photo{height:100px;background:linear-gradient(150deg,var(--photo-b),var(--photo-a))}
  .service-name{background:var(--green-deep);color:#fff;font-size:11px;font-weight:700;text-transform:uppercase;text-align:center;padding:8px 6px}
  .service-more{font-size:10px;color:var(--muted);text-align:center;margin-top:6px}

  .clients{height:130px;background:var(--mist);padding-top:18px}
  .client-row{display:flex;justify-content:center;gap:50px;margin-top:22px}
  .client-name{display:flex;align-items:center;gap:8px;font-size:15px;font-weight:700;color:var(--muted)}
  .client-mark{width:12px;height:12px;background:var(--muted)}

  .cases{height:200px;background:var(--green-deep);display:flex;align-items:center;gap:50px;padding:0 120px;color:#fff}
  .cases-copy{flex:1}
  .cases .section-title{color:#fff;text-align:left}
  .cases .section-title::after{background:#fff;margin:8px 0 0}
  .cases-text{font-size:12px;line-height:1.6;margin-top:16px;color:#d8e4e0}
  .cases-btn{display:inline-block;margin-top:14px;background:var(--green-soft);color:#fff;font-size:10px;font-weight:700;padding:7px 18px;letter-spacing:1px}
  .cases-photo{width:420px;height:150px;background:linear-gradient(140deg,#9fb0b6,var(--photo-a))}

  .contact{height:220px;padding-top:16px}
  .contact-body{display:flex;justify-content:center;gap:120px;margin-top:16px}
  .contact-form{width:380px;display:flex;flex-direction:column;gap:7px}
  .field{border:1px solid var(--line);font-size:10px;color:var(--muted);padding:6px 10px}
  .field.message{height:34px}
  .send-btn{align-self:flex-end;background:var(--green);color:#fff;font-size:10px;font-weight:700;padding:6px 18px}
  .contact-info{width:300px;display:flex;flex-direction:column;gap:10px}
  .info-line{display:flex;align-items:center;gap:10px;font-size:11px;color:var(--ink)}
  .info-line svg{width:14px;height:14px;flex:none}

  .site-footer{height:30px;background:var(--green-deep);color:#cfdcd8;font-size:10px;display:flex;align-items:center;justify-content:space-between;padding:0 60px}
</style>
</head>
<body>
<div class="page">
  <header class="site-header">
    <div class="brand"><span class="brand-dot"></span>Nuvira Projetos</div>
    <nav class="main-nav">
      <a class="active" href="#">Início</a><a href="#">Sobre</a><a href="#">Serviços</a><a href="#">Clientes</a><a href="#">Cases</a><a href="#">Contato</a>
    </nav>
  </header>

  <section class="hero">
    <div class="hero-photo" role="img" aria-label="Foto de subestação elétrica com estruturas metálicas"></div>
    <svg class="hero-cut" viewBox="0 0 1200 90" preserveAspectRatio="none"><polygon points="0,90 1200,0 1200,90" fill="#ffffff"/></svg>
    <div class="hero-copy">
      <h1 class="hero-title">Gerenciamento &amp; Consultoria<br>de Projetos</h1>
      <span class="hero-btn">SAIBA MAIS</span>
    </div>
  </section>

  <section class="services">
    <h2 class="section-title">Serviços</h2>
    <div class="service-grid">
      <article class="service-card"><div class="service-photo" role="img" aria-label="Foto de equipamentos elétricos"></div><div class="service-name">Gestão de Obras</div><p class="service-more">Saiba mais</p></article>
      <article class="service-card"><div class="service-photo" role="img" aria-label="Foto de linhas de transmissão"></div><div class="service-name">Consultoria Elétrica</div><p class="service-more">Saiba mais</p></article>
      <article class="service-card"><div class="service-photo" role="img" aria-label="Foto de canteiro de obras ao entardecer"></div><div class="service-name">Planejamento Técnico</div><p class="service-more">Saiba mais</p></article>
      <article class="service-card"><div class="service-photo" role="img" aria-label="Foto de estrutura industrial"></div><div class="service-name">Projetos Executivos</div><p class="service-more">Saiba mais</p></article>
    </div>
  </section>

  <section class="clients">
    <h2 class="section-title">Clientes</h2>
    <div class="client-row">
      <span class="client-name"><span class="client-mark"></span>Altavolt</span>
      <span class="client-name"><span class="client-mark"></span>Energis</span>
      <span class="client-name"><span class="client-mark"></span>Pontual</span>
      <span class="client-name"><span class="client-mark"></span>Tecnor</span>
      <span class="client-name"><span class="client-mark"></span>Vetra</span>
    </div>
  </section>

  <section class="cases">
    <div class="cases-copy">
      <h2 class="section-title">Cases de Sucesso</h2>
      <p class="cases-text">Acompanhamos projetos de energia do planejamento à entrega, com equipes ágeis, prazos cumpridos e soluções flexíveis para cada cliente e cada etapa da obra.</p>
      <span class="cases-btn">VER MAIS</span>
    </div>
    <div class="cases-photo" role="img" aria-label="Foto de subestação em área aberta"></div>
  </section>

  <section class="contact">
    <h2 class="section-title">Contato</h2>
    <div class="contact-body">
      <form class="contact-form">
        <div class="field">Nome</div>
        <div class="field">E-mail</div>
        <div class="field message">Mensagem</div>
        <span class="send-btn">ENVIAR</span>
      </form>
      <div class="contact-info">
        <div class="brand"><span class="brand-dot"></span>Nuvira Projetos</div>
        <div class="info-line"><svg viewBox="0 0 16 16"><path d="M4 1h3l1 4-2 1a9 9 0 0 0 4 4l1-2 4 1v3a2 2 0 0 1-2 2A13 13 0 0 1 2 3a2 2 0 0 1 2-2z" fill="#2c6b5c"/></svg>(11) 4000-1234</div>
        <div class="info-line"><svg viewBox="0 0 16 16"><rect x="1" y="3" width="14" height="10" fill="none" stroke="#2c6b5c" stroke-width="1.5"/><path d="M1 3l7 6 7-6" fill="none" stroke="#2c6b5c" stroke-width="1.5"/></svg>contato@nuviraprojetos.com.br</div>
        <div class="info-line"><svg viewBox="0 0 16 16"><path d="M8 1a5 5 0 0 1 5 5c0 4-5 9-5 9S3 10 3 6a5 5 0 0 1 5-5z" fill="#2c6b5c"/><circle cx="8" cy="6" r="2" fill="#fff"/></svg>Rua das Palmeiras, 120 – São Paulo</div>
      </div>
    </div>
  </section>

  <footer class="site-footer">
    <span>© 2024 Nuvira Projetos. Todos os direitos reservados.</span>
    <span>Gerenciamento &amp; Consultoria</span>
  </footer>
</div>
</body>
</html>
```